Mind-Body Counsellor Needs a Flyer

Please refer to the attachment for the content of the flyer.

I need a 99x210mm double sided leaflet design for my Vancouver BC based counselling practice.

I am a somatic counsellor who helps people with chronic body symptoms transform their experiences by working on the emotional, historical and relational aspects of the body difficulty. I use art, movement and body awareness in my practice to support and follow my client's unique process. I believe in the power and creativity of the body symptoms itself to show a needed direction. My clients report that this process is transformational, and helps change the relationship they have with their symptom. Often the symptom itself is relieved as the person integrates the needed changes in their life. People say they feel more alive, whole and aware of their overall path in life through this process. I am trained in Flowfield Awareness Method.

I will be bringing the flyer to Doctors and Massage Therapists offices to get new referrals of clients who seek pain management with no relief in the conventional medical system. I would like designs that show diversity of cultures and body types. The final design should communicate professionalism, creativity, hope and healing.

Target Market(s)

Physician and health practitioners who can refer clients with difficulties relating to anxiety, depression, and medically untreatable body symptoms

Industry/Entity Type

Counsellor

Font styles to use
Sans Serif

Colors
ffcf3e
ffc214
fbee3d
cadf82
acd037
9bcb3c

Requirements
Must have
• Visual impact
• A sense of hope and transformation
• Sense of professionalism and creativity
Nice to have
• May or may not include people - but if it does, must represent diverse genders, ages, races, abilities etc.
Should not have
• Too text heavy
• For some reason the uploader is not working - I'll get the text uploaded by tomorrow!

```html
<!DOCTYPE html>
<html lang="en">
<head>
<meta charset="utf-8">
<title>Maren Holloway – Counselling Leaflet</title>
<link href="https://fonts.googleapis.com/css2?family=Catamaran:wght@400;500;600&family=Kaushan+Script&display=swap" rel="stylesheet">
<style>
  :root{
    --sun:#fdd13c;
    --sun-deep:#ffc214;
    --lemon:#fbee3d;
    --lime:#acd037;
    --leaf:#0fae4b;
    --grass:#6fbf44;
    --chartreuse:#d4e02a;
    --ink:#1c1c1c;
    --slate:#5b5b5b;
    --quali:#3aae3a;
    --page:#ece8e1;
  }
  *{box-sizing:border-box;margin:0;padding:0}
  html,body{width:1200px;height:1200px;overflow:hidden;background:var(--page);font-family:"Catamaran",sans-serif;color:var(--ink)}
  .sheet{position:absolute;top:80px;width:499px;height:1038px;background:#fff;overflow:hidden;box-shadow:0 2px 10px rgba(0,0,0,.12)}
  .front{left:66px}
  .back{left:631px}

  /* front */
  .front-header{position:absolute;left:0;top:0;width:100%;height:66px;background:var(--sun);border-bottom:4px solid var(--lime);
    font-weight:600;font-size:16px;padding:29px 0 0 28px}
  .hero-photo{position:absolute;left:0;top:66px;width:100%;height:290px;
    background:radial-gradient(ellipse at 55% 25%,#fffbd8 0%,#e9e48a 30%,#b9c83a 60%,#6f8a1f 100%)}
  .hero-title{position:absolute;left:32px;top:245px;font-family:"Kaushan Script",cursive;color:#fff;font-size:38px;line-height:48px;
    text-shadow:0 2px 6px rgba(0,0,0,.45)}
  .stripe{position:absolute;left:0;width:100%;height:11px;display:flex}
  .stripe span{display:block;height:100%}
  .front .stripe{top:356px}
  .lower-photo{position:absolute;left:0;top:560px;width:100%;height:478px;
    background:linear-gradient(180deg,#fff 0%,#fde9b0 18%,#f7b733 42%,#e07a12 62%,#4a3a2a 82%,#1f2a3a 100%)}
  .intro{position:absolute;left:44px;width:411px;text-align:center;font-size:12.5px;line-height:19px}
  .intro.one{top:402px}
  .intro.two{top:479px}
  .quali-title{position:absolute;left:28px;top:609px;color:var(--quali);font-size:20px;font-weight:500}
  ul{list-style:none}
  li{position:relative;padding-left:15px}
  li::before{content:"•";position:absolute;left:0}
  .quali-list{position:absolute;left:29px;top:640px;font-size:12.5px;line-height:17px}
  .quali-list li{margin-bottom:7px}
  .suited{position:absolute;left:0;top:776px;width:350px;height:195px;background:rgba(253,222,40,.93);border-radius:0 8px 8px 0;padding:21px 0 0 29px}
  .suited h2{font-size:16px;font-weight:600;line-height:19px;margin-bottom:7px}
  .suited li{font-size:12.5px;line-height:22px}

  /* back */
  .back .stripe{top:0;height:23px}
  .badge{position:absolute;left:206px;top:54px;width:88px;height:88px;border-radius:50%;background:var(--sun-deep)}
  .back-title{position:absolute;left:0;top:162px;width:100%;text-align:center;color:var(--slate);font-size:31px;font-weight:600;line-height:34px}
  .quote{position:absolute;left:36px;width:430px;font-size:15px;line-height:24px;color:var(--slate)}
  .cite{position:absolute;right:39px;font-size:15px;font-weight:500;color:var(--slate);text-align:right}
  .divider{position:absolute;left:23px;width:453px;border-top:2px dashed var(--chartreuse)}
  .contact{position:absolute;left:23px;top:731px;width:453px;height:307px;background:var(--sun);border-radius:8px 8px 0 0;text-align:center}
  .contact-head{position:absolute;top:40px;left:30px;right:30px;display:flex;align-items:center;gap:12px;font-size:19px;font-weight:500}
  .contact-head::before,.contact-head::after{content:"";flex:1;border-top:2px solid var(--ink)}
  .contact-name{position:absolute;top:88px;width:100%;font-size:22px;font-weight:600;line-height:26px}
  .contact-name small{display:block;font-size:19px;font-weight:500}
  .contact-line{position:absolute;width:100%;font-size:19px;font-weight:500;display:flex;justify-content:center;align-items:center;gap:10px}
  .contact-line svg{width:20px;height:20px;fill:var(--ink)}
</style>
</head>
<body>

<section class="sheet front">
  <div class="front-header">Maren Holloway , MA, MEd, Registered Clinical Counsellor</div>
  <div class="hero-photo" role="img" aria-label="Photo of a diverse family jumping with joined hands in a sunlit green park"></div>
  <div class="hero-title">Making Life<br>More Meaningful</div>
  <div class="stripe">
    <span style="width:25%;background:var(--lime)"></span><span style="width:31%;background:var(--leaf)"></span><span style="width:10.5%;background:var(--grass)"></span><span style="width:17%;background:var(--chartreuse)"></span><span style="width:16.5%;background:var(--grass)"></span>
  </div>

  <div class="lower-photo" role="img" aria-label="Photo of a person rising from the sea with arms raised against a golden sunset"></div>

  <p class="intro one">Maren Holloway is a Registered Clinical Counsellor with over 16 years of experience helping people find meaning and transformation in life’s most difficult circumstances.</p>
  <p class="intro two">She uses cutting edge psychotherapeutic approaches, along with warmth, compassion and humour. Her specialty training in somatic approaches to healing is particularly useful for people with chronic health problems, recovering from accidents, or seeking better awareness of the connection between their minds and their bodies.</p>

  <h2 class="quali-title">Qualifications:</h2>
  <ul class="quali-list">
    <li>MA Health Promotion</li>
    <li>MEd Counselling Psychology</li>
    <li>MA Flowfield Awareness Method<br>and Conflict Facilitation</li>
    <li>Level 1 Somatic Resonance Therapy</li>
  </ul>

  <div class="suited">
    <h2>Uniquely Suited for Clients<br>who struggle with:</h2>
    <ul>
      <li>Anxiety or depression related to health concerns</li>
      <li>Trauma-related difficulties of mind, body or spirit</li>
      <li>Chronic, undiagnosed somatic complaints</li>
      <li>Nightmares</li>
      <li>Relationship conflicts</li>
    </ul>
  </div>
</section>

<section class="sheet back">
  <div class="stripe">
    <span style="width:15%;background:var(--lime)"></span><span style="width:37%;background:var(--leaf)"></span><span style="width:12.5%;background:var(--grass)"></span><span style="width:20.5%;background:var(--chartreuse)"></span><span style="width:15%;background:var(--grass)"></span>
  </div>
  <div class="badge">
    <svg viewBox="0 0 88 88" width="88" height="88" aria-hidden="true">
      <g fill="#fff">
        <path d="M26 40 L50 30 L54 58 L30 52 Z"/>
        <rect x="20" y="40" width="9" height="13" rx="2" transform="rotate(-10 24 46)"/>
        <path d="M33 52 L38 53 L40 64 L35 65 Z"/>
        <ellipse cx="52" cy="44" rx="4" ry="14" transform="rotate(-10 52 44)"/>
      </g>
      <g stroke="#fff" stroke-width="2.5" stroke-linecap="round">
        <line x1="60" y1="36" x2="66" y2="32"/><line x1="62" y1="44" x2="69" y2="44"/><line x1="57" y1="29" x2="59" y2="23"/>
      </g>
    </svg>
  </div>
  <h1 class="back-title">What Maren’s<br>Clients Say:</h1>

  <p class="quote" style="top:266px">“ Maren helped me radically shift how I relate to my body difficulties. They used to be monsters that scared me, now I see them as allies helping me bring my passion out into the world”</p>
  <p class="cite" style="top:366px">– Participant in “Body Wisdom” Course</p>
  <div class="divider" style="top:418px"></div>

  <p class="quote" style="top:455px">“I used to have nightmares every night. Working with Maren helped me find the power in my dreams, my history, my struggle to be who I am in the world. Now my dreams are guides telling me I’m on the right track.”</p>
  <p class="cite" style="top:563px">- F. D. Business Owner, Trauma Survivor</p>
  <div class="divider" style="top:622px"></div>

  <p class="quote" style="top:653px">“Working with Maren is magic!!”</p>
  <p class="cite" style="top:685px">- D.B. Medical Lab Assistant</p>

  <div class="contact">
    <div class="contact-head">CONTACT INFORMATION</div>
    <div class="contact-name">Maren Holloway,<small>MA, MEd Counselling Psychology</small></div>
    <div class="contact-line" style="top:157px">
      <svg viewBox="0 0 24 24"><path d="M2 5h20v14H2z M2 5l10 8 10-8" fill="var(--ink)"/><path d="M3 6.5l9 7 9-7" stroke="var(--sun)" stroke-width="1.6" fill="none"/></svg>
      maren@hollowaycounselling.ca
    </div>
    <div class="contact-line" style="top:196px">
      <svg viewBox="0 0 24 24"><path d="M6.6 10.8a15 15 0 0 0 6.6 6.6l2.2-2.2a1 1 0 0 1 1-.25 11.4 11.4 0 0 0 3.6.57 1 1 0 0 1 1 1V20a1 1 0 0 1-1 1A17 17 0 0 1 3 4a1 1 0 0 1 1-1h3.5a1 1 0 0 1 1 1c0 1.25.2 2.45.57 3.57a1 1 0 0 1-.25 1z"/></svg>
      604-555-0182
    </div>
    <div class="contact-line" style="top:235px">
      <svg viewBox="0 0 24 24"><path d="M12 2a7 7 0 0 0-7 7c0 5.2 7 13 7 13s7-7.8 7-13a7 7 0 0 0-7-7zm0 9.5A2.5 2.5 0 1 1 12 6.5a2.5 2.5 0 0 1 0 5z"/></svg>
      Vancouver, BC
    </div>
  </div>
</section>

</body>
</html>
```